Elegant Business Card for Technology Company

Client is a supplier of innovative industrial communications and automation equipment since 2002. This contest is to gather fresh ideas for a redesign of the existing business card. Client is looking for design that best communicates tagline "Industrial Networking and Computing Specialist".

Design submissions should look modern, clean, elegant and professional. It should not be cluttered. Use white as the primary colour. Orange and black as secondary colour. Refer to jpeg File 1 on the current design.

Fonts used by Client used include Arial Regular, Arial Black, Roboto Regular, Roboto Black and Lato.

The winning design will be sent for offset printing using super white 250gsm artcard paper (open for suggestions).

Target Market(s)

System Engineers, Project Managers, Purchasing Managers from companies providing engineering services for Smart Cities.

Industry/Entity Type

Information Technology

Contact Information for Business Card

Refer to PDF File 3 for Business Card Details. Priority of short contact information would be as follows Name > Job Title > Email > Mobile > Web > Tel > Fax > Business Address >UEN (UEN represents company registration number)

Font styles to use
Sans Serif

Colors
ffffff
f37122
000000
5c5c5c

Requirements
Must have
• Refer to AI File 2 (Company Logo) & PDF File 3 (Information on Namecard)
Should not have
• No QR codes
• No Social Media Icons
• Do not create full Black or Orange colour background

```html
<!DOCTYPE html>
<html lang="en">
<head>
<meta charset="utf-8">
<title>Korvane Asia Pacific – Business Card</title>
<link href="https://fonts.googleapis.com/css2?family=Source+Sans+3:wght@400;600;700;900&display=swap" rel="stylesheet">
<style>
  :root {
    --white: #ffffff;
    --orange: #f37122;
    --black: #000000;
    --grey: #5c5c5c;
    --peach: #f9b98f;
    --stage: #e9e7e4;
  }
  * { box-sizing: border-box; margin: 0; padding: 0; }
  html, body { width: 1200px; height: 800px; overflow: hidden; }
  body {
    background: var(--stage);
    font-family: "Source Sans 3", Arial, sans-serif;
    color: var(--black);
    display: flex;
    align-items: center;
    justify-content: center;
    gap: 40px;
  }
  .card {
    position: relative;
    width: 540px;
    height: 324px;
    background: var(--white);
    overflow: hidden;
    box-shadow: 0 4px 14px rgba(0,0,0,0.12);
  }
  .card-footer { position: absolute; left: 0; right: 0; bottom: 0; height: 28px; }
  .card-footer svg { display: block; }
  .web {
    position: absolute; right: 22px; bottom: 6px;
    color: var(--white); font-size: 15px; letter-spacing: 0.5px;
  }

  /* front */
  .brand { position: absolute; left: 26px; top: 40px; display: flex; align-items: center; gap: 10px; }
  .brand-dot { width: 30px; height: 30px; border-radius: 50%; background: var(--orange); }
  .brand-name { font-size: 46px; font-weight: 900; color: var(--black); letter-spacing: -1px; line-height: 1; }
  .person { position: absolute; left: 28px; top: 150px; }
  .person-native { font-size: 24px; letter-spacing: 8px; font-weight: 400; }
  .person-name { font-size: 24px; font-weight: 700; margin-top: 6px; line-height: 1; }
  .person-title { font-size: 15px; color: var(--orange); margin-top: 2px; }
  .company { position: absolute; left: 300px; top: 128px; font-size: 17px; font-weight: 700; color: var(--orange); }
  .company-rule { position: absolute; left: 300px; right: 0; top: 152px; height: 1px; background: var(--black); }
  .details { position: absolute; right: 22px; top: 160px; text-align: right; font-size: 13px; line-height: 1.35; color: var(--black); }
  .details .address { margin-bottom: 10px; }

  /* back */
  .back-rule { position: absolute; left: 0; width: 400px; top: 40px; height: 1px; background: var(--black); }
  .back-company { position: absolute; right: 140px; top: 58px; font-size: 17px; font-weight: 700; color: var(--orange); border-bottom: 1px solid var(--black); padding-bottom: 2px; }
  .tagline { position: absolute; left: 28px; top: 92px; font-size: 16px; font-weight: 700; }
  .services { position: absolute; left: 28px; top: 120px; list-style: none; font-size: 14px; line-height: 1.4; }
  .services li::before { content: ""; display: inline-block; width: 6px; height: 6px; border-radius: 50%; background: var(--orange); margin-right: 8px; vertical-align: middle; }
  .dot-field { position: absolute; right: -90px; top: 30px; width: 220px; height: 220px; border-radius: 50%; background: var(--peach); }
</style>
</head>
<body>

<section class="card card-front">
  <div class="brand">
    <span class="brand-dot"></span>
    <span class="brand-name">KORVANE</span>
  </div>
  <div class="person">
    <div class="person-native">中文名</div>
    <div class="person-name">Daniel Koh</div>
    <div class="person-title">Sales Manager</div>
  </div>
  <div class="company">Korvane Asia Pacific Pte Ltd</div>
  <div class="company-rule"></div>
  <div class="details">
    <div class="address">28 Kestrel Road Harbourview Park #05-12 (Block B)<br>Singapore 419731</div>
    <div>Mobile Number +65 9123 4567</div>
    <div>Telephone +65 6234 5170</div>
    <div>Fax +65 6234 5189</div>
    <div>Email hello@korvane.sg</div>
    <div>UEN No 200207415K</div>
  </div>
  <div class="card-footer">
    <svg width="540" height="28" viewBox="0 0 540 28">
      <rect x="0" y="18" width="540" height="10" fill="var(--black)"/>
      <polygon points="335,0 540,0 540,28 315,28" fill="var(--orange)"/>
    </svg>
    <span class="web">www.korvane.sg</span>
  </div>
</section>

<section class="card card-back">
  <div class="back-rule"></div>
  <div class="back-company">Korvane Asia Pacific Pte Ltd</div>
  <div class="tagline">Industrial Networking and Computing Specialist</div>
  <ul class="services">
    <li>Industrial Ethernet / Wireless / Cellular</li>
    <li>Industrial and Embedded Computing</li>
    <li>Serial / Fieldbus Connectivity</li>
    <li>IP Video Surveillance</li>
    <li>Remote Automation</li>
  </ul>
  <div class="dot-field" role="img" aria-label="Decorative field of soft orange dots"></div>
  <div class="card-footer">
    <svg width="540" height="28" viewBox="0 0 540 28">
      <rect x="0" y="18" width="540" height="10" fill="var(--black)"/>
      <polygon points="335,0 540,0 540,28 315,28" fill="var(--orange)"/>
    </svg>
    <span class="web">www.korvane.sg</span>
  </div>
</section>

</body>
</html>
```